タイトルは『集い準備応援戦団 ホール任せマン 集い段取り快勝手引きブック」とします。表紙、タイトルには戦隊もののヒーローを彷彿とさせるようなデザインを希望します。

ゴルフコンペの幹事業務がどんな内容なのかを細かく丁寧に説明し、尚且つ弊社のサービスがどんなメリットがあるのかを事細かに説明する内容です。サービスの概要を伝える見開き2ページの漫画と、詳細を記したデータを貼付します。

①表紙→②漫画→③詳細

このうち①、③を合わせてお願いしたいと思います。貼付内容の著作権は弊社にありますので、パンフレット内で画像等自由に使用してください。

ページ数に拘りはないのでわかりやすい内容にするために増えてしまっても問題ないです。

当方のコンセプトをよく理解し、さらに発展させてくれました。やりとりの中で当方の漠然としたイメージがどんどん具体化していき気持ちよかったです。最終的には12ページに渡る非常に素晴らしいものを納品していただきました。

確定が遅くなり申し訳ございませんでした。どれも素晴らしいご提案でした。また機会がありましたら宜しくお願い致します。

```html
<!DOCTYPE html>
<html lang="ja">
<head>
<meta charset="utf-8">
<title>集い段取り快勝手引きブック</title>
<link rel="stylesheet" href="https://fonts.googleapis.com/css2?family=Dela+Gothic+One&family=M+PLUS+Rounded+1c:wght@700;800&family=Noto+Sans+JP:wght@500;700;900&display=swap">
<style>
  :root {
    --sky-top: #dfeaf3;
    --sky-low: #c6d9e6;
    --hill: #5d7f4a;
    --forest: #3f6a34;
    --fairway: #74a94a;
    --fairway-deep: #5b9037;
    --brand-red: #a01e2a;
    --hero-red: #e0161d;
    --hero-yellow: #ffe100;
    --hero-blue: #1d4fc4;
    --ink: #1a1a1a;
    --white: #ffffff;
  }
  * { margin: 0; padding: 0; box-sizing: border-box; }
  html, body { width: 849px; height: 1200px; overflow: hidden; background: var(--white); }
  .cover {
    position: relative;
    width: 849px;
    height: 1200px;
    overflow: hidden;
    font-family: "Noto Sans JP", sans-serif;
  }
  .course-scene {
    position: absolute;
    inset: 0;
    background:
      linear-gradient(180deg,
        var(--sky-top) 0%,
        var(--sky-low) 22%,
        var(--hill) 27%,
        var(--forest) 38%,
        var(--fairway) 46%,
        var(--fairway-deep) 100%);
  }
  .edge-band {
    position: absolute;
    left: 0;
    width: 100%;
    background: var(--brand-red);
  }
  .edge-band--top { top: 0; height: 8px; }
  .edge-band--bottom { bottom: 0; height: 14px; }

  .squad-name {
    position: absolute;
    top: 106px;
    width: 100%;
    text-align: center;
    font-family: "Noto Sans JP", sans-serif;
    font-weight: 900;
    font-size: 40px;
    line-height: 1.2;
    color: var(--hero-yellow);
    -webkit-text-stroke: 6px var(--hero-red);
    paint-order: stroke fill;
    letter-spacing: 3px;
  }
  .hero-title {
    position: absolute;
    top: 160px;
    width: 100%;
    text-align: center;
    font-family: "Dela Gothic One", sans-serif;
    font-size: 98px;
    line-height: 1.2;
    color: var(--hero-blue);
    -webkit-text-stroke: 12px var(--white);
    paint-order: stroke fill;
    letter-spacing: 2px;
    text-shadow: 4px 5px 0 var(--ink);
  }
  .hero-title__accent { color: var(--hero-red); }
  .hero-subtitle {
    position: absolute;
    top: 290px;
    width: 100%;
    text-align: center;
    font-family: "M PLUS Rounded 1c", sans-serif;
    font-weight: 800;
    font-size: 25px;
    color: var(--white);
    -webkit-text-stroke: 5px var(--ink);
    paint-order: stroke fill;
  }
  .guide-band {
    position: absolute;
    top: 338px;
    left: 0;
    width: 100%;
    height: 62px;
    background: rgba(255,255,255,0.78);
    display: flex;
    align-items: center;
    padding-left: 78px;
  }
  .guide-band__text {
    font-weight: 900;
    font-size: 30px;
    color: var(--ink);
    letter-spacing: 1px;
  }
  .squad-members {
    position: absolute;
    left: 432px;
    top: 402px;
    width: 356px;
    height: 240px;
    border-radius: 12px;
    background: linear-gradient(180deg, #3a3d45 0%, #2a2c33 70%, #1f2127 100%);
    opacity: 0.85;
  }
  .golfer {
    position: absolute;
    left: 38px;
    top: 660px;
    width: 310px;
    height: 445px;
    border-radius: 16px;
    background: linear-gradient(180deg, #d8423a 0%, #c9302b 45%, #f2f2f2 55%, #e6e6e6 100%);
    opacity: 0.85;
  }
  .badges {
    position: absolute;
    top: 848px;
    left: 548px;
    display: flex;
    gap: 12px;
  }
  .badge {
    width: 134px;
    height: 134px;
    border-radius: 50%;
    background: var(--white);
    border: 3px solid var(--hero-red);
    display: flex;
    align-items: center;
    justify-content: center;
    text-align: center;
    padding: 14px;
    font-weight: 700;
    font-size: 15px;
    line-height: 1.45;
    color: var(--hero-red);
  }
  .club-mark {
    position: absolute;
    bottom: 26px;
    width: 100%;
    display: flex;
    justify-content: center;
    align-items: center;
    gap: 10px;
  }
  .club-mark__square {
    width: 36px;
    height: 36px;
    background: var(--brand-red);
  }
  .club-mark__name {
    font-weight: 700;
    font-size: 18px;
    line-height: 1.25;
    color: var(--brand-red);
  }
</style>
</head>
<body>
  <main class="cover">
    <div class="course-scene" role="img" aria-label="緑の山並みと青空を背景にしたゴルフ場のフェアウェイの風景"></div>
    <div class="edge-band edge-band--top"></div>

    <h1>
      <span class="squad-name">集い準備応援戦団</span>
      <span class="hero-title">ホール<span class="hero-title__accent">任せ</span>マン</span>
    </h1>
    <p class="hero-subtitle">Gathering Prep Hero Squad</p>

    <div class="guide-band">
      <p class="guide-band__text">集い段取り快勝手引きブック</p>
    </div>

    <div class="squad-members" role="img" aria-label="ヒーローのポーズをとるスーツ姿の4人の幹事代行チームのイラスト"></div>
    <div class="golfer" role="img" aria-label="赤いシャツでスイングするゴルファーのイラスト"></div>

    <div class="badges">
      <p class="badge">初心者だけでなくベテラン幹事さんにもおすすめ！</p>
      <p class="badge">他のゴルフ場でコンペ企画する時も活用できる！</p>
    </div>

    <div class="club-mark">
      <span class="club-mark__square"></span>
      <span class="club-mark__name">MIDORINOMORI<br>みどりの森カントリークラブ</span>
    </div>

    <div class="edge-band edge-band--bottom"></div>
  </main>
</body>
</html>
```